Retro Label for old fashioned soda

We need a label for soda we are having private labeled for our retro, 1950's ice cream shop www.maplewhirlcones.com I don't want the label to look like something from 2017 with a retro feel, but more like an original (possibly kinda cheesy) label you'd see from the 1950's with some of the old catch lines like "tastes great", "invigorating" or "it is refreshing!" The prominent brand should be the name of our ice cream shop, The Maple Whirl. the soda is also pure cane sugar so it might be good to have that on somewhere

Label size is 2.4" wide by 4" tall. Here is an example of some retro labels from findoramap. I attached on file to this contest but there are more here: https://www.findoramap.net/search?q=retro+soda+label

The label will be the same for all the flavors with the exception of the flavor name changing somewhere on the label. These are the flavors

Root Beer
Orange
Black Cherry
Lemonade
Raspberry Lime -Rickey
White Birch Beer
Lemon Iced Tea
Vanilla Cream
Orange Cream
Sarsaparilla
Ginger Ale

Industry/Entity Type

Shop

Colors

Designer to choose colors to be used in the design.

Requirements
Must have
• retro feel. authentic old fashioned look

```html
<!DOCTYPE html>
<html lang="en">
<head>
<meta charset="utf-8">
<title>The Maple Whirl – Root Beer Label</title>
<link rel="stylesheet" href="https://fonts.googleapis.com/css2?family=Old+Standard+TT:wght@400;700&family=Bodoni+Moda:wght@400&display=swap">
<style>
  :root {
    --page: #f2f1ee;
    --label-tan: #dccfac;
    --frame-orange: #d8712e;
    --brand-blue: #3b5899;
    --flavor-green: #3f9a4c;
    --mountain-green: #3e9a4a;
    --snow: #f1efe8;
    --tagline-ink: #4a4038;
  }
  html, body {
    margin: 0;
    padding: 0;
    width: 1200px;
    height: 818px;
    overflow: hidden;
    background: var(--page);
  }
  .canvas {
    position: relative;
    width: 1200px;
    height: 818px;
  }
  .soda-label {
    position: absolute;
    left: 100px;
    top: 99px;
    width: 1000px;
    height: 620px;
    background: var(--label-tan);
  }
  .soda-label svg {
    position: absolute;
    inset: 0;
    width: 1000px;
    height: 620px;
  }
  .frame-line { fill: none; stroke: var(--frame-orange); }
  .corner-dot { fill: var(--frame-orange); }
  .brand-arch {
    font-family: "Old Standard TT", Georgia, serif;
    font-weight: 700;
    font-size: 60px;
    letter-spacing: 4px;
    fill: var(--brand-blue);
  }
  .flavor-name {
    font-family: "Bodoni Moda", "Times New Roman", serif;
    font-weight: 400;
    font-size: 96px;
    fill: var(--flavor-green);
  }
  .flavor-rule { stroke: var(--flavor-green); stroke-width: 3; }
  .tagline {
    font-family: "Old Standard TT", Georgia, serif;
    font-weight: 400;
    font-size: 26px;
    fill: var(--tagline-ink);
  }
  .tagline-dot { fill: var(--frame-orange); }
  .mountain-art {
    position: absolute;
    left: 440px;
    top: 300px;
    width: 160px;
    height: 99px;
    background: linear-gradient(to bottom, var(--snow) 0%, var(--mountain-green) 30%, var(--mountain-green) 100%);
  }
</style>
</head>
<body>
<main class="canvas">
  <section class="soda-label">
    <svg viewBox="0 0 1000 620" aria-label="The Maple Whirl Root Beer label">
      <defs>
        <path id="brand-arc" d="M 200 500 A 368 368 0 0 1 905 420"/>
      </defs>
      <rect class="frame-line" x="22" y="22" width="956" height="576" stroke-width="3"/>
      <rect class="frame-line" x="36" y="36" width="928" height="548" stroke-width="12"/>
      <rect class="frame-line" x="52" y="52" width="896" height="516" stroke-width="3"/>
      <circle class="corner-dot" cx="86" cy="86" r="14"/>
      <circle class="corner-dot" cx="914" cy="86" r="14"/>
      <circle class="corner-dot" cx="86" cy="534" r="14"/>
      <circle class="corner-dot" cx="914" cy="534" r="14"/>

      <text class="brand-arch" text-anchor="middle">
        <textPath href="#brand-arc" startOffset="50%">THE MAPLE WHIRL</textPath>
      </text>

      <line class="flavor-rule" x1="300" y1="400" x2="890" y2="400"/>
      <text class="flavor-name" x="320" y="490" textLength="560" lengthAdjust="spacingAndGlyphs">ROOT BEER</text>

      <circle class="tagline-dot" cx="336" cy="526" r="6"/>
      <text class="tagline" x="350" y="535" textLength="180" lengthAdjust="spacingAndGlyphs">TASTES GREAT</text>
      <circle class="tagline-dot" cx="656" cy="526" r="6"/>
      <text class="tagline" x="670" y="535" textLength="170" lengthAdjust="spacingAndGlyphs">REFRESHING!</text>
    </svg>
    <div class="mountain-art" role="img" aria-label="Illustration of green snow-capped mountain peaks"></div>
  </section>
</main>
</body>
</html>
```